Adventure and fiction Brazilian Rainforest Secrets book called Tin Lantern*

I want the reader to be curious about the cover. I want the cover to make you want to see the contents of the book. Both physical and digital on shelves or on websites. Eye-grabbing and eye-popping. Something that would make me abandon anything I was doing to go to the shelf and flip through the book.

I'd like a bright and live green cover. With rainforest. With small human figure in the middle of the forest.

If possible, use image composition IOI as per attachment.

Please hide a camouflaged UFO for internal joke.

Note: The name of the book in Portuguese is Casa Lunar (Tin Lantern).

Note 2: The book is set on an island in the Atlantic Ocean. If you want you can include beaches, sea and hills in the distance.

Note 3: The book is not for children.

Target Market(s)

Velorix pageon, E-book, Websites, libraries

Requirements
Must have
• Something that would make me abandon anything I was doing to go to the shelf and flip through the book.
Nice to have
• Small human figure in the middle of the rainforest.
• Bright and live Green cover (If you got any new ideas of colors to stand out, please go ahead.)
• Hidden camouflaged UFO for internal joke
• Composition IOI
• Beaches, sea and hills in the distance
• Something attractive. Irresistible.
Should not have
• It's not a children's book - Please no kids themes

```html
<!DOCTYPE html>
<html lang="en">
<head>
<meta charset="utf-8">
<title>Casa Lunar – Book Cover</title>
<link rel="stylesheet" href="https://fonts.googleapis.com/css2?family=Marcellus&family=Rubik+Dirt&family=Jost:wght@400&display=swap">
<style>
  :root {
    --backdrop: #bfc6c6;
    --sky-deep: #132824;
    --sky-night: #1d3a36;
    --cloud-green: #5fa88a;
    --cloud-pale: #8fc4ae;
    --haze: #a9c2c4;
    --hill-blue: #3a5a6a;
    --field-green: #4f9a2e;
    --field-bright: #6dab2a;
    --field-gold: #c9a548;
    --lake-blue: #3c6a80;
    --ink-light: #f4f6f2;
    --spine-dark: #2c4a3a;
  }
  * { margin: 0; padding: 0; box-sizing: border-box; }
  html, body { width: 1200px; height: 800px; overflow: hidden; }
  body {
    background: var(--backdrop);
    position: relative;
    font-family: "Jost", sans-serif;
  }
  .front-cover, .back-cover, .spine {
    position: absolute;
    top: 102px;
    height: 612px;
    overflow: hidden;
  }
  .front-cover { left: 216px; width: 348px; }
  .back-cover { left: 603px; width: 324px; }
  .spine { left: 927px; width: 28px; }

  .cover-art {
    position: absolute; inset: 0;
    background:
      radial-gradient(ellipse 40% 18% at 15% 6%, rgba(143,196,174,.75), transparent 70%),
      radial-gradient(ellipse 35% 14% at 20% 38%, rgba(95,168,138,.6), transparent 70%),
      radial-gradient(ellipse 45% 12% at 45% 55%, rgba(169,194,196,.9), transparent 75%),
      radial-gradient(ellipse 22% 40% at 42% 100%, rgba(201,165,72,.95), transparent 75%),
      radial-gradient(ellipse 40% 20% at 90% 85%, rgba(201,165,72,.55), transparent 75%),
      linear-gradient(180deg,
        var(--sky-night) 0%, var(--sky-deep) 28%, var(--cloud-green) 31%, var(--sky-night) 35%,
        var(--hill-blue) 45%, var(--haze) 52%, var(--field-bright) 58%,
        var(--field-green) 75%, var(--field-green) 100%);
  }
  .back-art {
    position: absolute; inset: 0;
    background:
      radial-gradient(ellipse 60% 18% at 45% 8%, rgba(169,210,190,.85), transparent 70%),
      radial-gradient(ellipse 50% 14% at 70% 25%, rgba(143,196,174,.6), transparent 70%),
      radial-gradient(ellipse 70% 10% at 50% 60%, rgba(60,106,128,.9), transparent 75%),
      linear-gradient(180deg,
        var(--cloud-green) 0%, var(--cloud-pale) 10%, var(--cloud-green) 30%,
        #4a7a5a 48%, var(--hill-blue) 56%, var(--lake-blue) 62%,
        var(--field-bright) 72%, var(--field-green) 100%);
  }
  .spine-art {
    position: absolute; inset: 0;
    background: linear-gradient(180deg, var(--cloud-green) 0%, #4a7a5a 40%, var(--spine-dark) 55%, var(--field-green) 80%, var(--field-green) 100%);
  }

  .author-name {
    position: absolute; top: 52px; left: 0; right: 0;
    text-align: center;
    font-family: "Marcellus", serif;
    font-size: 33px; letter-spacing: 2px;
    color: var(--ink-light);
  }
  .book-title {
    position: absolute; top: 300px; left: 0; right: 0;
    text-align: center;
    font-family: "Rubik Dirt", sans-serif;
    font-weight: 400;
    font-size: 66px; line-height: 66px;
    color: var(--ink-light);
    text-transform: uppercase;
    transform: scale(1, 1.4);
    transform-origin: top center;
  }

  .blurb {
    position: absolute; top: 126px; left: 4px; right: 26px;
    color: var(--ink-light);
    font-size: 10.6px; line-height: 14px;
  }
  .blurb p + p { margin-top: 12px; }

  .spine-title, .spine-author {
    position: absolute; left: 50%;
    writing-mode: vertical-rl;
    transform: translateX(-50%);
    color: var(--ink-light);
  }
  .spine-title {
    top: 66px;
    font-family: "Rubik Dirt", sans-serif;
    font-size: 15px; letter-spacing: 1px;
  }
  .spine-author {
    top: 438px;
    font-family: "Marcellus", serif;
    font-size: 10px; letter-spacing: 1px;
  }
</style>
</head>
<body>
  <section class="front-cover">
    <div class="cover-art" role="img" aria-label="Night sky with green clouds over a hidden saucer, a lone tree on a hill, and a small figure walking down a golden dirt path through bright green fields"></div>
    <div class="author-name">AUTHOR NAME</div>
    <h1 class="book-title">Casa<br>Lunar</h1>
  </section>

  <section class="back-cover">
    <div class="back-art" role="img" aria-label="Misty green sky over a calm lake, dark treeline and rolling grass fields"></div>
    <div class="blurb">
      <p>Lorem ipsum dolor sit amet, consectetur adipiscing elit, sed do eiusmod tempor incididunt ut labore et dolore magna aliqua. Pellentesque massa placerat duis ultricies lacus sed turpis. Mattis aliquam faucibus purus in massa. Volutpat ac tincidunt vitae semper. Dictum at tempor commodo ullamcorper a lacus vestibulum sed arcu. Posuere sollicitudin aliquam ultrices sagittis. Dui sapien eget mi proin sed libero enim. Egestas sed tempus urna et pharetra pharetra massa. Ornare quam viverra orci sagittis eu volutpat. Suspendisse ultrices gravida dictum fusce ut placerat. Tempus iaculis urna id volutpat lacus laoreet. Sed lectus vestibulum mattis ullamcorper velit sed ullamcorper. Interdum velit laoreet id donec. Odio eu feugiat pretium nibh ipsum consequat. Velit dignissim sodales ut eu sem integer vitae justo eget. Nibh tortor id aliquet lectus proin nibh nisl condimentum id. Pharetra sit amet aliquam id diam maecenas ultricies. Ac placerat vestibulum lectus mauris ultrices eros.</p>
      <p>Sed vulputate odio ut enim blandit volutpat maecenas. Ac tincidunt vitae semper quis lectus nulla at volutpat. Ut diam quam nulla porttitor massa id neque aliquam. Suscipit adipiscing bibendum est ultricies integer quis auctor. Senectus et netus et malesuada fames ac turpis egestas. Tortor dignissim convallis aenean et tortor at risus. Turpis egestas sed tempus urna et pharetra pharetra massa massa. Fusce ut placerat orci nulla pellentesque. Adipiscing elit duis tristique sollicitudin.</p>
    </div>
  </section>

  <section class="spine">
    <div class="spine-art" role="img" aria-label="Green sky and field texture"></div>
    <div class="spine-title">CASA LUNAR</div>
    <div class="spine-author">AUTHOR NAME</div>
  </section>
</body>
</html>
```